construction company offering modern and striking homes and apartments

I need a card design for my new construction company called Tallow Constructions (vic) Pty Ltd.
We build everything from multi home development sites to modern and edgy apartment complexes.
I am open to any colors used as long as it stands out and doesn't look cheap. I want the final design to show my prospective clients I am a professional construction company

Industry/Entity Type

Construction

```html
<!DOCTYPE html>
<html lang="en">
<head>
<meta charset="utf-8">
<title>Tallow Constructions – Business Card</title>
<link rel="stylesheet" href="https://fonts.googleapis.com/css2?family=Montserrat:wght@300&family=Lato:wght@400;700&display=swap">
<style>
  :root {
    --backdrop: #1f1f1f;
    --card-dark: #2e2c2c;
    --card-light: #f7f7f5;
    --ink: #1d1b1b;
    --ink-soft: #6b6b6b;
    --mark-light: #d9d9d9;
    --text-light: #bdbdbd;
    --faint: rgba(255, 255, 255, 0.06);
    --badge-fill: #dcdcd8;
  }
  * { box-sizing: border-box; margin: 0; padding: 0; }
  html, body { width: 1200px; height: 997px; overflow: hidden; }
  body {
    background: var(--backdrop);
    display: flex;
    align-items: center;
    justify-content: center;
    gap: 40px;
    font-family: "Lato", Arial, sans-serif;
  }
  .card {
    position: relative;
    width: 540px;
    height: 300px;
    overflow: hidden;
    border-radius: 2px;
  }

  /* Back of card */
  .card-back { background: var(--card-dark); }
  .card-back .faint-disc {
    position: absolute;
    width: 240px; height: 240px;
    right: 40px; top: -110px;
    border-radius: 50%;
    background: var(--faint);
  }
  .card-back .brand {
    position: absolute;
    left: 44px; bottom: 52px;
    display: flex; align-items: center; gap: 16px;
  }
  .card-back .brand-dot {
    width: 62px; height: 62px; border-radius: 50%;
    background: var(--mark-light);
  }
  .brand-name {
    font-family: "Montserrat", Arial, sans-serif;
    font-weight: 300;
    font-size: 21px;
    line-height: 1.1;
    letter-spacing: 1.5px;
    text-transform: uppercase;
  }
  .card-back .brand-name { color: var(--text-light); }

  /* Front of card */
  .card-front { background: var(--card-light); color: var(--ink); }
  .card-front .brand {
    position: absolute;
    left: 46px; top: 48px;
    display: flex; align-items: center; gap: 18px;
  }
  .card-front .brand-dot {
    width: 62px; height: 62px; border-radius: 50%;
    background: var(--ink);
  }
  .card-front .brand-name { color: var(--ink); }
  .rule {
    position: absolute;
    height: 1.5px;
    background: var(--ink);
  }
  .rule-brand { left: 140px; right: 40px; top: 128px; }
  .rule-person { left: 196px; width: 130px; top: 178px; }

  .person { position: absolute; left: 44px; top: 166px; }
  .person-name { font-weight: 700; font-size: 17px; color: var(--ink); }
  .person-role {
    font-size: 9.5px; letter-spacing: 0.8px;
    text-transform: uppercase; color: var(--ink-soft);
    margin-top: 2px;
  }

  .badges {
    position: absolute; right: 40px; top: 152px;
    display: flex; align-items: center; gap: 26px;
  }
  .badge {
    background: var(--badge-fill);
  }
  .badge-square { width: 40px; height: 40px; }
  .badge-wide { width: 84px; height: 40px; }

  .contacts {
    position: absolute; left: 44px; top: 212px;
    list-style: none;
    font-size: 11.5px; color: var(--ink-soft);
  }
  .contacts li {
    display: flex; align-items: center; gap: 12px;
    height: 24px;
  }
  .contacts svg { width: 13px; height: 13px; fill: var(--ink); flex: none; }
</style>
</head>
<body>
  <section class="card card-back" aria-label="Card back">
    <div class="faint-disc"></div>
    <div class="brand">
      <div class="brand-dot"></div>
      <p class="brand-name">Tallow<br>Constructions</p>
    </div>
  </section>

  <section class="card card-front" aria-label="Card front">
    <div class="brand">
      <div class="brand-dot"></div>
      <p class="brand-name">Tallow<br>Constructions</p>
    </div>
    <div class="rule rule-brand"></div>

    <div class="person">
      <p class="person-name">Daniel Tallow</p>
      <p class="person-role">Managing Director</p>
    </div>
    <div class="rule rule-person"></div>

    <div class="badges" aria-label="Industry memberships">
      <div class="badge badge-square"></div>
      <div class="badge badge-wide"></div>
    </div>

    <ul class="contacts">
      <li>
        <svg viewBox="0 0 16 16" aria-hidden="true"><path d="M1 5c0-2 2-3 7-3s7 1 7 3v1h-4V4.5H5V6H1zM3 8l2-2h6l2 2v6H3zm5 1.5a2 2 0 1 0 0 4 2 2 0 0 0 0-4z"/></svg>
        0400 318 274
      </li>
      <li>
        <svg viewBox="0 0 16 16" aria-hidden="true"><path d="M1 3h14v10H1zm1.5 1.5v.3L8 9l5.5-4.2v-.3zm0 2.2v4.8h11V6.7L8 11z"/></svg>
        daniel@tallowconstructions.com
      </li>
      <li>
        <svg viewBox="0 0 16 16" aria-hidden="true"><path d="M8 1.5 0.5 8h2.3v6.5h4V10h2.4v4.5h4V8h2.3z"/></svg>
        27 Ridge Lane Northvale Vic 3999
      </li>
    </ul>
  </section>
</body>
</html>
```